Wedding Day Custom Wine Label - Tasmanian (Tamar Valley) wine

I am looking for a custom design that will be put on a wine label to commemorate a very good friend's wedding day.

We will need to be able to take the design and print it on to sticker labels that we can put on to wine bottles.

The bride and groom have asked for a simplistic label design (see example image attached). We need two labels. One for "Pinot Noir" wine and the other for "Chardonnay" wine. We would like the label to say:

The Hartwell's
Pinot Noir
2023
Tamar Valley

and for for the other wine variety:

The Hartwell's
Chardonnay
2023
Tamar Valley

smaller text below to say:

13.5% ALC/VOL 750ML
MEGAN & LIAM - 31.10.2024

I am happy to consider other variations - the bride & groom would prefer something minimalistic. Elegant and classy.

Target Market(s)

the bride & groom

Requirements
Must have
• Wedding date (31.10.2024). Wine type (Pinot Noir or Chardonnay).
Should not have
• images not essential

```html
<!DOCTYPE html>
<html lang="en">
<head>
<meta charset="utf-8">
<title>The Hartwell's – Wedding Wine Labels</title>
<link href="https://fonts.googleapis.com/css2?family=Alice&family=Kaushan+Script&display=swap" rel="stylesheet">
<style>
  :root {
    --page-bg: #efefef;
    --label-cream: #f7f5e7;
    --ink: #111111;
    --rule: #3a3a3a;
    --label-shadow: rgba(0, 0, 0, 0.10);
  }
  * { margin: 0; padding: 0; box-sizing: border-box; }
  html, body {
    width: 1200px;
    height: 800px;
    overflow: hidden;
    background: var(--page-bg);
  }
  .canvas {
    position: relative;
    width: 1200px;
    height: 800px;
  }
  .wine-label {
    position: absolute;
    top: 101px;
    width: 460px;
    height: 598px;
    background: var(--label-cream);
    box-shadow: 0 4px 14px var(--label-shadow);
    color: var(--ink);
    font-family: "Alice", Georgia, serif;
  }
  .wine-label--pinot { left: 110px; }
  .wine-label--chardonnay { left: 630px; }

  .couple-title {
    position: absolute;
    left: 0;
    right: 0;
    top: 108px;
    text-align: center;
    font-family: "Kaushan Script", cursive;
    line-height: 0.8;
    transform: rotate(-8deg);
  }
  .couple-title__article {
    display: block;
    font-size: 74px;
    margin-left: 36px;
  }
  .couple-title__surname {
    display: block;
    font-size: 78px;
    margin-top: -4px;
  }

  .wine-details {
    position: absolute;
    left: 0;
    right: 0;
    top: 280px;
    text-align: center;
    font-size: 32px;
    line-height: 33px;
    letter-spacing: 0.5px;
  }

  .wedding-block {
    position: absolute;
    left: 85px;
    right: 81px;
    top: 426px;
    height: 68px;
    border-top: 1px solid var(--rule);
    border-bottom: 1px solid var(--rule);
    text-align: center;
    padding-top: 12px;
    font-size: 19px;
    line-height: 26px;
    letter-spacing: 1px;
  }

  .bottle-facts {
    position: absolute;
    left: 79px;
    right: 76px;
    top: 535px;
    display: flex;
    justify-content: space-between;
    font-size: 18px;
    letter-spacing: 0.5px;
  }
</style>
</head>
<body>
<main class="canvas">

  <section class="wine-label wine-label--pinot">
    <h1 class="couple-title">
      <span class="couple-title__article">The</span>
      <span class="couple-title__surname">Hartwell's</span>
    </h1>
    <div class="wine-details">
      <p class="wine-details__variety">Pinot Noir</p>
      <p class="wine-details__vintage">2023</p>
      <p class="wine-details__region">Tamar Valley</p>
    </div>
    <div class="wedding-block">
      <p class="wedding-block__couple">MEGAN &amp; LIAM</p>
      <p class="wedding-block__date">31.10.2024</p>
    </div>
    <div class="bottle-facts">
      <span class="bottle-facts__abv">13.5% ALC/VOL</span>
      <span class="bottle-facts__volume">750ML</span>
    </div>
  </section>

  <section class="wine-label wine-label--chardonnay">
    <h1 class="couple-title">
      <span class="couple-title__article">The</span>
      <span class="couple-title__surname">Hartwell's</span>
    </h1>
    <div class="wine-details">
      <p class="wine-details__variety">Chardonnay</p>
      <p class="wine-details__vintage">2023</p>
      <p class="wine-details__region">Tamar Valley</p>
    </div>
    <div class="wedding-block">
      <p class="wedding-block__couple">MEGAN &amp; LIAM</p>
      <p class="wedding-block__date">31.10.2024</p>
    </div>
    <div class="bottle-facts">
      <span class="bottle-facts__abv">13.5% ALC/VOL</span>
      <span class="bottle-facts__volume">750ML</span>
    </div>
  </section>

</main>
</body>
</html>
```